Wine Label for Sparkling Pinot Noir

Design a label for Keloru Sparkling Pinot Noir 2016.
It is a single label with main area and more discreet required wine details on one side (must be readable, see example pdf). All elements are displayed in the example pdf.

Logo is our Thai Lady 'Shield', which can be modified as required (flowers removed, color changed etc). Brand name is 'Keloru'

Label needs to be professional and elegant with a slight Asian influence.

Dimensions of the label are: 130mm wide x 80mm height
SVG final product
Leave a bleed edge around (ie. dont put text right to the edge)
Printing will be 4CP, so can be creative as you like with colors and design.

Do a google for 'Stone in River Sparkling Pinot Noir' for some inspiration!

Target Market(s)

Wine drinkers in middle to upper class Restaurants

Logo Text

Keloru - Sparkling Pinot Noir - 2016

Requirements
Must have
• Elegant & Simple with provided text in example pdf
Nice to have
• We are located in an historical mining area.
• Slight Asian influence through our logo.

```html
<!DOCTYPE html>
<html lang="en">
<head>
<meta charset="utf-8">
<title>Keloru Sparkling Pinot Noir 2016 – Front Label</title>
<link rel="stylesheet" href="https://fonts.googleapis.com/css2?family=Questrial&family=Pinyon+Script&family=Italianno&family=Cormorant+Garamond:ital,wght@1,700&display=swap">
<style>
  :root {
    --page-bg: #d7e7f0;
    --label-bg: #fbfdfe;
    --label-tint: #eef5f9;
    --gold: #d1a92d;
    --gold-text: #c79a2a;
    --seal-dark: #111010;
    --cream: #f6efd8;
    --ink: #1b1b1b;
  }
  * { margin: 0; padding: 0; box-sizing: border-box; }
  html, body {
    width: 1200px;
    height: 1200px;
    overflow: hidden;
    background: var(--page-bg);
  }
  .sheet {
    position: relative;
    width: 1200px;
    height: 1200px;
  }
  .sheet-title {
    position: absolute;
    top: 118px;
    left: 0;
    width: 100%;
    text-align: center;
    font-family: "Questrial", sans-serif;
    font-size: 44px;
    color: var(--ink);
    letter-spacing: 0.5px;
  }
  .label {
    position: absolute;
    left: 235px;
    top: 284px;
    width: 735px;
    height: 726px;
    background: var(--label-bg);
    overflow: hidden;
  }
  .label-pattern {
    position: absolute;
    inset: 0;
    background: linear-gradient(180deg, var(--label-tint), var(--label-bg) 50%, var(--label-tint));
  }
  .gold-band {
    position: absolute;
    left: 0;
    top: 82px;
    width: 100%;
    height: 108px;
    background: var(--gold);
    box-shadow: 0 10px 18px rgba(160, 140, 90, 0.18);
  }
  .brand-seal {
    position: absolute;
    left: 285px;
    top: 52px;
    width: 172px;
    height: 172px;
    border-radius: 50%;
    background: var(--seal-dark);
    display: flex;
    align-items: center;
    justify-content: center;
  }
  .brand-seal-name {
    font-family: "Cormorant Garamond", serif;
    font-style: italic;
    font-weight: 700;
    font-size: 34px;
    color: var(--gold);
  }
  .brand-name {
    position: absolute;
    top: 218px;
    left: 0;
    width: 100%;
    text-align: center;
    font-family: "Italianno", cursive;
    font-size: 170px;
    line-height: 1;
    color: var(--cream);
  }
  .wine-style {
    position: absolute;
    left: 0;
    width: 100%;
    text-align: center;
    font-family: "Pinyon Script", cursive;
    color: var(--ink);
    line-height: 1;
  }
  .wine-style--sparkling { top: 410px; font-size: 66px; }
  .wine-style--variety { top: 500px; font-size: 72px; }
  .vintage {
    position: absolute;
    top: 618px;
    left: 0;
    width: 100%;
    text-align: center;
    font-family: "Cormorant Garamond", serif;
    font-style: italic;
    font-weight: 700;
    font-size: 48px;
    color: var(--gold-text);
  }
</style>
</head>
<body>
  <main class="sheet">
    <h1 class="sheet-title">Front - face of the bottle</h1>
    <section class="label">
      <div class="label-pattern" role="img" aria-label="Fine pattern of pale blue dots across the label background"></div>
      <div class="gold-band"></div>
      <div class="brand-seal"><span class="brand-seal-name">Keloru</span></div>
      <p class="brand-name">Keloru</p>
      <p class="wine-style wine-style--sparkling">Sparkling</p>
      <p class="wine-style wine-style--variety">Pinot Noir</p>
      <p class="vintage">2016</p>
    </section>
  </main>
</body>
</html>
```